New Business Cards for Parvel

About Parvel:
At Parvel, we're more than just a company—we're a force for positive change in the staffing industry. Our brand is our heartbeat, and we need a designer who can translate that into every design element.

The Project:
We're revamping our business cards and need your artistic flair to make them stand out. Here's what we're looking for:

- Incorporate our existing brand elements (logo, colours, fonts) into the design.
- Craft a design that's sleek, professional, and memorable.
- Provide options for different layouts and finishes.
- Collaborate closely with our team to ensure the final product exceeds expectations.

Please note: For general text, we use Avenir. The brand guidelines are slightly out of date and don't have correct imaging. Colours are correct though.

```html
<!DOCTYPE html>
<html lang="en">
<head>
<meta charset="utf-8">
<title>Parvel Business Card</title>
<link href="https://fonts.googleapis.com/css2?family=Nunito+Sans:wght@400;600;700;800&display=swap" rel="stylesheet">
<style>
  :root {
    --page-bg: #e9e6e8;
    --card-light: #f6f1f2;
    --brand-purple: #4d145a;
    --brand-pink: #d6156e;
    --text-light: #ffffff;
  }
  html, body {
    margin: 0;
    padding: 0;
    width: 1200px;
    height: 900px;
    overflow: hidden;
    background: var(--page-bg);
    font-family: "Nunito Sans", Arial, sans-serif;
  }
  .card {
    position: absolute;
    left: 110px;
    top: 147px;
    width: 980px;
    height: 606px;
    background: var(--card-light);
    box-shadow: 0 12px 34px rgba(60, 20, 60, 0.18);
    overflow: hidden;
  }
  .card-top {
    position: absolute;
    inset: 0 0 auto 0;
    height: 327px;
  }
  .brand-name {
    position: absolute;
    top: 78px;
    left: 0;
    right: 0;
    text-align: center;
    font-size: 104px;
    font-weight: 800;
    color: var(--brand-purple);
    line-height: 1;
    letter-spacing: 1px;
  }
  .tagline {
    position: absolute;
    top: 220px;
    left: 0;
    right: 0;
    text-align: center;
    font-size: 29px;
    font-weight: 400;
    color: var(--brand-purple);
    letter-spacing: 0.5px;
  }
  .accent-rule {
    position: absolute;
    top: 327px;
    left: 0;
    right: 0;
    height: 8px;
    background: var(--brand-pink);
  }
  .card-bottom {
    position: absolute;
    top: 335px;
    left: 0;
    right: 0;
    bottom: 0;
    background: var(--brand-purple);
    color: var(--text-light);
  }
  .identity {
    position: absolute;
    right: 516px;
    top: 72px;
    text-align: right;
  }
  .person-name {
    font-size: 46px;
    font-weight: 800;
    line-height: 1;
  }
  .person-role {
    font-size: 29px;
    font-weight: 400;
    margin-top: 2px;
  }
  .divider {
    position: absolute;
    left: 484px;
    top: 62px;
    width: 2px;
    height: 94px;
    background: var(--text-light);
  }
  .contacts {
    position: absolute;
    left: 508px;
    top: 56px;
    margin: 0;
    padding: 0;
    list-style: none;
    font-size: 29px;
    line-height: 36px;
  }
  .contacts li {
    display: flex;
    align-items: center;
    gap: 8px;
  }
  .contacts svg {
    width: 27px;
    height: 27px;
    flex: none;
  }
  .address {
    position: absolute;
    left: 0;
    right: 0;
    top: 202px;
    text-align: center;
    font-size: 27px;
  }
</style>
</head>
<body>
  <div class="card">
    <div class="card-top">
      <div class="brand-name">Parvel</div>
      <div class="tagline">people at the core</div>
    </div>
    <div class="accent-rule"></div>
    <div class="card-bottom">
      <div class="identity">
        <div class="person-name">Daniel Morris</div>
        <div class="person-role">Managing Director</div>
      </div>
      <div class="divider"></div>
      <ul class="contacts">
        <li>
          <svg viewBox="0 0 24 24" fill="none" stroke="#fff" stroke-width="2" aria-hidden="true"><path d="M5 3h4l2 5-2.5 1.5a11 11 0 0 0 6 6L16 13l5 2v4a2 2 0 0 1-2 2A16 16 0 0 1 3 5a2 2 0 0 1 2-2z"/><path d="M14 3a7 7 0 0 1 7 7M14 7a3 3 0 0 1 3 3"/></svg>
          <span>021-555 018 342</span>
        </li>
        <li>
          <svg viewBox="0 0 24 24" aria-hidden="true"><rect x="2" y="5" width="20" height="14" fill="#fff"/><path d="M2 5l10 8 10-8" fill="none" stroke="#4d145a" stroke-width="1.6"/></svg>
          <span>hello@parvelmail.com</span>
        </li>
        <li>
          <svg viewBox="0 0 24 24" fill="none" stroke="#fff" stroke-width="1.6" aria-hidden="true"><circle cx="12" cy="12" r="10"/><ellipse cx="12" cy="12" rx="4.5" ry="10"/><path d="M2 12h20M4 7h16M4 17h16"/></svg>
          <span>www.parvelstaff.com</span>
        </li>
      </ul>
      <div class="address">87, Harbour Lane Suite 12 30418,Northland</div>
    </div>
  </div>
</body>
</html>
```